Redesign of page from emergency manual

Please redesign this PDF to look better. Please don't include any stock photos. It must be legible. Making some words bold is probably a good idea.

Here are some things I like :

https://tarrowbooks.com.au/collections/frontpage/products/the-plk-v2-ebook

https://img-cd.vostramediafiles.com/qa-ejkwPLOTYY_SuCKbZNu411Qwgjv8YssPxEdzXN93hDkSRjLXK8WmfgbmrJW4ZZ3yUPK=w1052-h592-rw

```html
<!DOCTYPE html>
<html lang="en">
<head>
<meta charset="utf-8">
<title>Hypertension, Acute – Emergency Manual Page 12</title>
<link href="https://fonts.googleapis.com/css2?family=Exo+2:wght@400;500;600;700;800&display=swap" rel="stylesheet">
<style>
  :root {
    --navy: #0e3557;
    --navy-deep: #0a2a47;
    --sky: #1fa3e0;
    --sky-soft: #35b0e8;
    --ice: #e9f6fc;
    --row-grey: #ededed;
    --page-grey: #e6e6e6;
    --ink: #1c2d3f;
    --white: #ffffff;
    --silver-hi: #f4f6f8;
    --silver-lo: #a9b2bb;
  }
  * { box-sizing: border-box; margin: 0; padding: 0; }
  html, body { width: 1200px; height: 1200px; overflow: hidden; }
  body {
    background: var(--page-grey);
    font-family: "Exo 2", "Segoe UI", sans-serif;
    color: var(--ink);
    position: relative;
  }
  .page {
    position: absolute; left: 98px; top: 208px;
    width: 1014px; height: 784px;
    background: var(--white);
    overflow: hidden;
  }
  .header-band {
    position: absolute; left: 0; top: 0; width: 965px; height: 272px;
    background: var(--sky);
  }
  .title-block {
    position: absolute; left: 0; top: 0; width: 340px; height: 253px;
    background: var(--navy);
    text-align: center;
    padding-top: 44px;
  }
  .title-main {
    font-weight: 800; letter-spacing: 0.5px; line-height: 1;
    background: linear-gradient(180deg, var(--silver-hi) 0%, var(--silver-lo) 100%);
    -webkit-background-clip: text; background-clip: text; color: transparent;
  }
  .title-main .line-1 { display: block; font-size: 40px; }
  .title-main .line-2 { display: block; font-size: 52px; margin-top: 2px; }
  .title-rule { width: 230px; height: 2px; background: var(--sky); margin: 10px auto 14px; }
  .title-sub {
    color: var(--ice); font-weight: 700; font-size: 17px; line-height: 1.3;
    text-transform: uppercase; letter-spacing: 0.3px;
  }
  .intro {
    position: absolute; left: 372px; top: 18px; width: 580px;
    color: var(--white); font-size: 13.5px; font-weight: 600; line-height: 1.35;
  }
  .intro p { margin-bottom: 12px; }
  .intro ul { list-style: none; }
  .intro li::before { content: "• "; }
  .caution {
    position: absolute; left: 372px; top: 144px; width: 568px; height: 104px;
    background: var(--white); text-align: center;
    padding: 9px 20px 0;
    font-size: 13px; line-height: 1.35; color: var(--ink); font-weight: 600;
  }
  .caution-label { color: var(--sky); font-weight: 700; }
  .sidebar {
    position: absolute; left: 965px; top: 0; width: 49px; height: 784px;
    background: var(--navy);
  }
  .page-number {
    position: absolute; left: 9px; top: 25px; width: 31px; height: 31px;
    border-radius: 50%; background: var(--white); color: var(--navy);
    font-weight: 800; font-size: 16px; text-align: center; line-height: 31px;
  }
  .sidebar-title {
    position: absolute; left: 10px; top: 146px;
    writing-mode: vertical-rl; color: var(--white);
    font-weight: 700; font-size: 25px; letter-spacing: 1px;
  }
  .revision {
    position: absolute; left: 15px; top: 643px;
    writing-mode: vertical-rl; color: var(--white);
    font-size: 12px; font-weight: 500;
  }
  .bp-heading {
    position: absolute; left: 29px; top: 287px; width: 613px;
    text-align: center; color: var(--sky); font-weight: 700; font-size: 17.5px;
  }
  .bp-ranges { position: absolute; left: 30px; top: 320px; }
  .bp-ranges text { font-family: "Exo 2", sans-serif; }
  .dosing-table {
    position: absolute; left: 29px; top: 492px; width: 613px;
    border: 1.5px solid #4a4a4a; border-collapse: collapse;
    font-size: 13px;
  }
  .dosing-table th {
    height: 32px; font-size: 17px; font-weight: 600; color: var(--white);
    border: 5px solid var(--white); border-bottom-width: 3px;
  }
  .dosing-table th.col-action { background: var(--navy); width: 210px; }
  .dosing-table th.col-drug { background: var(--sky-soft); }
  .dosing-table td {
    vertical-align: top; padding: 10px 12px; line-height: 1.3;
    border-top: 1px solid #9a9a9a;
  }
  .dosing-table td.action { color: var(--navy); font-weight: 700; text-transform: uppercase; font-size: 13px; }
  .dosing-table td.drug { font-weight: 500; }
  .dosing-table tr.alt td { background: var(--row-grey); }
  .dosing-table ul { list-style: none; }
  .dosing-table li::before { content: "• "; color: var(--sky); }
  .dosing-table .indent { padding-left: 9px; }
  .wave-decor {
    position: absolute; left: 640px; top: 560px; width: 325px; height: 224px;
    background: radial-gradient(ellipse at 70% 70%, rgba(53,176,232,0.16) 0%, rgba(53,176,232,0) 70%);
  }
  .differential-head {
    position: absolute; left: 655px; top: 294px; width: 287px; height: 75px;
    background: var(--navy); color: var(--sky); text-align: center;
    font-weight: 700; font-size: 17.5px; line-height: 1.25; padding-top: 14px;
  }
  .differential-list {
    position: absolute; left: 682px; top: 382px; width: 260px;
    list-style: none; font-size: 13.5px; font-weight: 500; line-height: 1.3;
  }
  .differential-list li { position: relative; padding-left: 0; }
  .differential-list li::before { content: "•"; color: var(--sky); position: absolute; left: -9px; }
</style>
</head>
<body>
<main class="page">
  <div class="header-band"></div>

  <header class="title-block">
    <h1 class="title-main"><span class="line-1">HYPERTENSION</span><span class="line-2">ACUTE</span></h1>
    <div class="title-rule"></div>
    <p class="title-sub">Sustained high blood<br>pressure refractory to<br>treating reversible causes</p>
  </header>

  <section class="intro">
    <p>In pediatrics, hypertension is almost always treated by addressing likely causes such as light anesthesia or measurement error:</p>
    <ul>
      <li>Ensure correct BP cuff size: cuff bladder width ~ 40% of limb circumference</li>
      <li>Ensure arterial line transducer is at level of heart</li>
      <li>Consider placing arterial line if not already present</li>
    </ul>
  </section>

  <aside class="caution">
    <div class="caution-label">* CAUTION:</div>
    Anti-hypertensive drugs are almost never needed for routine pediatric cases. These medications are used almost exclusively for specialized cardiac, neurosurgical, or endocrine (pheochromocytoma) cases. Consult an expert before use. Rule-out increased ICP.
  </aside>

  <h2 class="bp-heading">HYPERTENSIVE BLOOD PRESSURE RANGE</h2>

  <svg class="bp-ranges" width="600" height="170" viewBox="0 0 600 170" aria-label="Hypertensive blood pressure range by age">
    <defs>
      <path id="arc-1" d="M 181.8 35.5 A 75 75 0 0 1 278.2 35.5"/>
      <path id="arc-2" d="M 328.8 35.5 A 75 75 0 0 1 425.2 35.5"/>
      <path id="arc-3" d="M 474.8 35.5 A 75 75 0 0 1 571.2 35.5"/>
      <clipPath id="c0"><circle cx="75" cy="93" r="69"/></clipPath>
      <clipPath id="c1"><circle cx="230" cy="93" r="69"/></clipPath>
      <clipPath id="c2"><circle cx="377" cy="93" r="69"/></clipPath>
      <clipPath id="c3"><circle cx="523" cy="93" r="69"/></clipPath>
    </defs>
    <g clip-path="url(#c0)"><rect x="0" y="20" width="150" height="74" fill="#35b0e8"/><rect x="0" y="94" width="150" height="80" fill="#0e3557"/></g>
    <g clip-path="url(#c1)"><rect x="155" y="20" width="150" height="74" fill="#35b0e8"/><rect x="155" y="94" width="150" height="80" fill="#0e3557"/></g>
    <g clip-path="url(#c2)"><rect x="302" y="20" width="150" height="74" fill="#35b0e8"/><rect x="302" y="94" width="150" height="80" fill="#0e3557"/></g>
    <g clip-path="url(#c3)"><rect x="448" y="20" width="150" height="74" fill="#35b0e8"/><rect x="448" y="94" width="150" height="80" fill="#0e3557"/></g>

    <text x="75" y="83" text-anchor="middle" fill="#0e3557" font-size="17" font-weight="600">SYSTOLIC</text>
    <text x="75" y="113" text-anchor="middle" fill="#ffffff" font-size="17" font-weight="600">DIASTOLIC</text>

    <text x="230" y="84" text-anchor="middle" fill="#0e3557" font-size="20" font-weight="600">&gt;97</text>
    <text x="230" y="118" text-anchor="middle" fill="#ffffff" font-size="20" font-weight="600">&gt;70</text>
    <text x="377" y="84" text-anchor="middle" fill="#0e3557" font-size="20" font-weight="600">&gt;105</text>
    <text x="377" y="118" text-anchor="middle" fill="#ffffff" font-size="20" font-weight="600">&gt;61</text>
    <text x="523" y="84" text-anchor="middle" fill="#0e3557" font-size="20" font-weight="600">&gt;113</text>
    <text x="523" y="118" text-anchor="middle" fill="#ffffff" font-size="20" font-weight="600">&gt;86</text>

    <text fill="#0e3557" font-size="15" font-weight="700"><textPath href="#arc-1" startOffset="50%" text-anchor="middle">NEWBORN</textPath></text>
    <text fill="#0e3557" font-size="15" font-weight="700"><textPath href="#arc-2" startOffset="50%" text-anchor="middle">AGE 1-3</textPath></text>
    <text fill="#0e3557" font-size="15" font-weight="700"><textPath href="#arc-3" startOffset="50%" text-anchor="middle">AGE 4-12</textPath></text>
  </svg>

  <table class="dosing-table">
    <thead>
      <tr><th class="col-action">ACTION</th><th class="col-drug">DRUG (IV DOSING)</th></tr>
    </thead>
    <tbody>
      <tr>
        <td class="action">Direct smooth<br>muscle relaxation</td>
        <td class="drug"><ul><li>Sodium nitroprusside 0.5-10 MICROgrams/kg/min</li><li>HydrALAZINE 0.1-0.2 mg/kg (adult dose 5-10 mg)</li></ul></td>
      </tr>
      <tr class="alt">
        <td class="action">β-Adrenergic<br>blockade</td>
        <td class="drug"><ul><li>Esmolol 100-500 MICROgrams/kg over 5 min, then</li><li>25-300 MICROgrams/kg/min</li><li>Labetalol (also α effect) 0.2-1 mg/kg q 10 min;</li></ul><div class="indent">0.4-3 mg/kg/hour (infusion)</div></td>
      </tr>
      <tr>
        <td class="action">Calcium channel<br>blockade</td>
        <td class="drug"><ul><li>niCARdapine 0.5-5 MICROgrams/kg/min</li><li>Clevidipine 0.5-3.5 MICROgrams/kg/min</li></ul></td>
      </tr>
      <tr class="alt">
        <td class="action">DL-Dopamine agonist</td>
        <td class="drug"><ul><li>Fenoldopam 0.2-0.8 MICROgrams/kg/min</li></ul></td>
      </tr>
    </tbody>
  </table>

  <div class="wave-decor" role="img" aria-label="Faint decorative flowing line pattern"></div>

  <h2 class="differential-head">CONSIDER DIFFERENTIAL<br>(PARTIAL):</h2>
  <ul class="differential-list">
    <li>Light anesthesia<br>(consider vaporizer or infusion<br>pump empty or malfunctioning)</li>
    <li>Hypercarbia</li>
    <li>Hypoxemia</li>
    <li>Arterial line transducer<br>too low or BP cuff too small</li>
    <li>Withdrawal (EtOH or opioid)</li>
    <li>Thyroid Storm</li>
    <li>Pheochromocytoma</li>
    <li>Drug Error</li>
  </ul>

  <nav class="sidebar">
    <div class="page-number">12</div>
    <div class="sidebar-title">HYPERTENSION, ACUTE</div>
    <div class="revision">Revision Feb 2020</div>
  </nav>
</main>
</body>
</html>
```